Packaging Label Design for Hair Styling Product

Our company is launching a new hair styling product in early June. Need a designer to help on the packaging label for the hair product.
For more details please go to our website velmarkhq.co

Target Market(s)

Male Age 13-34. Men who likes hair pomade/hair clay and other hair products

Industry/Entity Type

Hair And Beauty

Font styles to use
Sans Serif
Script

Requirements
Must have
• 1. Company logo must be used on circular and rectangular designs.
2.Company name must be used on rectangular design only.
3.Silver polyester label material will be used.
4.Colour theme shall be in colours such as “Black”, “Dark Grey” and “Silver”.
5.A black orchid artwork must be featured in the design.
6.The following copywriting must be included in the design,
7.“Lantern Grip Cream” on both circular and rectangular designs.
8. Velmark & Co. Logo

Circular Design Label
-Singapore’s Homebrew
-100mL
-Strong Hold| Charcoal Infused

Rectangular Design Label
-Ingredients: WATER (AQUA), EUPHORBIA CERIFERA (CANDELILLA) WAX, KAOLIN, PEG-40 HYDROGENATED CASTOR OIL, PRUNUS ARMENIACA (APRICOT) KERNEL OIL, CETEARYL ALCOHOL, CETEARYL GLUCOSIDE, RICINUS COMMUNIS (CASTOR) OIL, BENTONITE, FRAGRANCE, PHENOXYETHANOL, CAPRYLYL GLYCOL, SORBIC ACID, ACTIVATED CHARCOAL.
-Required to include a “12m” logo. *Refer to example design.
-“For best result, work a dime-sized amount between your palms and apply on blow-dried hair. Comb or shape your hair to desired style. Restyle anytime. Use more if needed.”
-High Texture| Matte Finish| Easy Wash-out| Easy Application| Featherweight
-Made in Singapore
-Velmark & Co. Pte. Ltd.
-742 Tessle Brook Road 4 #07-2861
Singapore 581462 | www.velmarkhq.co
Nice to have
• Reference from the previous hair clay design. Please refer to attached document.
Should not have
• Please refer to attachment on the colors.

```html
<!DOCTYPE html>
<html lang="en">
<head>
<meta charset="utf-8">
<title>Velmark &amp; Co. – Lantern Grip Cream Label</title>
<link rel="stylesheet" href="https://fonts.googleapis.com/css2?family=Cormorant+Garamond:wght@500&family=Josefin+Sans:wght@400&family=Montserrat:wght@400;500&family=Playball&display=swap">
<style>
  :root {
    --page-bg: #ffffff;
    --label-grey: #8b8b8e;
    --label-grey-light: #9a9a9d;
    --text-white: #ffffff;
    --text-cream: #efe3b8;
    --rule-light: rgba(255,255,255,0.75);
    --silver-dark: #8e8e92;
    --silver-light: #f4f4f6;
  }
  * { box-sizing: border-box; margin: 0; padding: 0; }
  html, body { width: 1200px; height: 931px; overflow: hidden; background: var(--page-bg); }
  .canvas { position: relative; width: 1200px; height: 931px; }

  .label-strip {
    position: absolute; left: 24px; top: 624px; width: 1146px; height: 122px;
    background: var(--label-grey); color: var(--text-white);
    font-family: "Montserrat", sans-serif; overflow: hidden;
  }
  .orchid-artwork {
    position: absolute; left: 430px; top: 0; width: 360px; height: 122px;
    background: radial-gradient(ellipse at 60% 45%, var(--label-grey-light) 0%, var(--label-grey) 70%);
  }

  .maker-block {
    position: absolute; left: 46px; top: 8px; width: 160px; text-align: center;
    font-size: 8.4px; line-height: 1.35;
  }
  .brand-mark {
    display: flex; align-items: center; justify-content: center; gap: 5px;
    font-size: 10px; font-weight: 500; letter-spacing: 0.5px; margin-bottom: 10px;
  }
  .brand-mark .dot { width: 8px; height: 8px; border-radius: 50%; background: var(--text-cream); }
  .maker-block .web { margin-top: 2px; }

  .usage-block {
    position: absolute; left: 232px; top: 12px; width: 170px; text-align: center;
    font-size: 8.4px; line-height: 1.3;
  }
  .usage-block .features { margin-top: 9px; color: var(--text-cream); }

  .product-title { position: absolute; left: 430px; top: 12px; width: 360px; text-align: center; }
  .product-title .company {
    font-family: "Cormorant Garamond", serif; font-weight: 500; font-size: 12px; letter-spacing: 1.5px;
  }
  .product-title .script-name {
    font-family: "Playball", cursive; font-size: 32px; line-height: 1; margin-top: 4px;
  }
  .product-title .product-type {
    font-family: "Josefin Sans", sans-serif; font-size: 25px; letter-spacing: 1.5px; line-height: 1; margin-top: 1px;
  }
  .silver-bar {
    position: absolute; left: 456px; top: 104px; width: 240px; height: 18px;
    background: linear-gradient(90deg, var(--silver-dark), var(--silver-light) 45%, #c7c7cb 70%, var(--silver-dark));
  }

  .ingredients-box {
    position: absolute; left: 744px; top: 14px; width: 362px; height: 70px;
    border: 1px solid var(--rule-light); padding: 5px 8px;
    font-size: 7.8px; line-height: 1.35; text-align: center; text-transform: uppercase;
  }
  .ingredients-box .lead { text-transform: none; }
  .volume { position: absolute; left: 880px; top: 96px; font-size: 10px; }
  .shelf-life-icon { position: absolute; left: 924px; top: 92px; }
</style>
</head>
<body>
<main class="canvas">
  <section class="label-strip" aria-label="Lantern Grip Cream wrap-around label">
    <div class="orchid-artwork" role="img" aria-label="Faint black orchid line artwork behind the product name"></div>

    <div class="maker-block">
      <div class="brand-mark"><span class="dot"></span><span>Velmark &amp; Co.</span></div>
      <p>Made in Singapore</p>
      <p>Velmark &amp; Co. Pte. Ltd.</p>
      <p>742 Tessle Brook Road 4 #07-2861</p>
      <p>Singapore 581462</p>
      <p class="web">www.velmarkhq.co</p>
    </div>

    <div class="usage-block">
      <p>For best result, work a dime-sized amount between your palms and apply on blow-dried hair. Comb or shape your hair to desired style. Restyle anytime. Use more if needed.</p>
      <div class="features">
        <p>• High Texture</p>
        <p>• Matte Finish • Easy Wash-out</p>
        <p>• Easy Application • Featherweight</p>
      </div>
    </div>

    <div class="product-title">
      <p class="company">VELMARK &amp; CO</p>
      <p class="script-name">Lantern</p>
      <p class="product-type">GRIP CREAM</p>
    </div>
    <div class="silver-bar"></div>

    <div class="ingredients-box">
      <p><span class="lead">Ingredients:</span> Water (Aqua), Euphorbia Cerifera (Candelilla) Wax, Kaolin, PEG-40 Hydrogenated Castor Oil, Prunus Armeniaca (Apricot) Kernel Oil, Cetearyl Alcohol, Cetearyl Glucoside, Ricinus Communis (Castor) Oil, Bentonite, Fragrance, Phenoxyethanol, Caprylyl Glycol, Sorbic Acid, Activated Charcoal.</p>
    </div>

    <p class="volume">100mL</p>
    <svg class="shelf-life-icon" width="24" height="20" viewBox="0 0 24 20" aria-label="12 months after opening">
      <path d="M3 6 L6 2 L18 2 L21 6 Z" fill="none" stroke="#fff" stroke-width="1"/>
      <rect x="3" y="6" width="18" height="12" fill="none" stroke="#fff" stroke-width="1"/>
      <text x="12" y="15.5" text-anchor="middle" font-family="Montserrat, sans-serif" font-size="7" fill="#fff">12M</text>
    </svg>
  </section>
</main>
</body>
</html>
```